Ledgerwise Reach - B2B Demand Generation Website Project

We need a fully functional website for www.ledgerwisereach.example. We are a B2B Demand Generation company, based in London, working with companies such as QRT, VKD, Norvex, Brindlow, Tarvo generating them sales leads for their sales teams. We run this through digital marketing newsletter promotions and have a network of websites. Content syndication, data, demand generation, online marketing. Our logo has just been redone (attached) and we have a holding page already which i would like to use the style / colours. Our logo is bright and vibrant but i dont want the site to be a rainbow. We are expensive, classy, professorial, B2B, intelligent.

Home
About Us
Our Services
Prospora & QA Technology
Intent Data
Testimonials
Contact Us
Updates

Target Market(s)

B2B Marketers (QRT, Velquarion, Tarvo, VKD, Opal Reach, Driftmoor, Harlow Quantis, Technology Companies, Data Companies, Marketing Teams, Tumbleden.

Industry/Entity Type

Marketing

Coding

Coded - Design and coding required

Number of Pages Required

5+ page

Font styles to use
Sans Serif

Requirements
Must have
• Home
About Us
Our Services
Prospora & QA Technology
Intent Data
Testimonials
Contact Us

Simple Pages.

Look classy, intelligent, data experts. I like the video homepages were the image moves at the top. Very soft animation.
Nice to have
• Websites i like:

https://www.vkd.example/
https://www.brevantor.example/
https://www.plumfieldsites.example.co.uk/

Ledgerwise Reach - The Demand Generation Company
Should not have
• Glimpsevault crap images

```html
<!DOCTYPE html>
<html lang="en">
<head>
<meta charset="utf-8">
<title>Ledgerwise Reach - The Demand Generation Company</title>
<link rel="stylesheet" href="https://fonts.googleapis.com/css2?family=Ubuntu:wght@300;400;500&family=Open+Sans:ital,wght@0,400;0,600;1,400&display=swap">
<style>
:root{
  --red:#d1262c;
  --navy:#0c2560;
  --blue:#1d4f91;
  --link:#2d5aa0;
  --ink:#333;
  --muted:#555;
  --grey:#f3f3f3;
  --line:#e6e6e6;
}
*{box-sizing:border-box;margin:0;padding:0}
html,body{width:1200px;height:3363px;overflow:hidden;background:#fff}
body{font-family:"Open Sans",sans-serif;color:var(--ink);position:relative}
.site{position:absolute;left:73px;top:245px;width:1054px;height:3015px;background:#fff;box-shadow:0 0 14px rgba(0,0,0,.08);overflow:hidden}
.abs{position:absolute}
h2,h3,.uh{font-family:"Ubuntu",sans-serif;font-weight:400}

/* header */
.masthead{position:absolute;left:0;top:0;width:100%;height:63px;background:#fff}
.brand{position:absolute;left:86px;top:16px;display:flex;align-items:center;gap:10px}
.brand-dot{width:30px;height:30px;border-radius:50%;background:var(--red)}
.brand-name{font-family:"Ubuntu",sans-serif;font-size:24px;color:var(--red);font-weight:400}
.nav{position:absolute;left:476px;top:24px;display:flex;gap:23px;font-size:12.5px;color:var(--muted)}
.nav .on{color:var(--link)}

/* hero */
.hero{position:absolute;left:0;top:63px;width:100%;height:430px;background:radial-gradient(ellipse at 30% 55%,#1c4a6e 0%,#0f2a44 40%,#0a1524 80%)}
.hero-curve{position:absolute;left:-60px;top:468px;width:1174px;height:160px;border-radius:50% 50% 0 0/100% 100% 0 0;background:#fff}
.hero h1{position:absolute;left:478px;top:90px;font-family:"Ubuntu",sans-serif;font-weight:400;font-size:30px;color:#fff}
.hero h1 span{color:#7fa6d8;text-decoration:underline;text-decoration-thickness:1px;text-underline-offset:5px}
.hero p{position:absolute;left:478px;top:154px;width:500px;font-size:12.5px;line-height:19px;color:#fff}
.btn-red{position:absolute;background:var(--red);color:#fff;border-radius:22px;display:flex;align-items:center;justify-content:center}
.hero .btn-red{left:478px;top:269px;width:148px;height:42px;font-size:14px}

/* about */
.about h2{position:absolute;left:89px;top:537px;font-size:25px;color:var(--red)}
.about p{position:absolute;left:89px;width:385px;font-size:12.2px;line-height:21px;color:var(--muted)}
.about .btn-red{left:89px;top:790px;width:98px;height:29px;font-size:11.5px}
.stat{position:absolute;width:213px;background:#fff;box-shadow:0 3px 14px rgba(0,0,0,.12);text-align:center}
.stat svg{display:block;margin:18px auto 0}
.stat .num{font-family:"Ubuntu",sans-serif;font-size:44px;color:var(--blue);line-height:52px;margin-top:6px}
.stat .cap{font-size:14px;color:#333}

/* partners */
.partners{position:absolute;left:0;top:942px;width:100%;height:323px;background:var(--grey)}
.section-title{position:absolute;width:100%;text-align:center;font-family:"Ubuntu",sans-serif;font-size:18px;color:var(--red)}
.partner-row{position:absolute;left:120px;top:155px;width:814px;display:flex;justify-content:space-between;align-items:center}
.partner{font-family:"Ubuntu",sans-serif;font-size:17px;font-weight:500;color:#1f3a66;width:100px;text-align:center}
.partner.ring{display:flex;align-items:center;justify-content:center;gap:6px}
.partner.ring i{width:14px;height:14px;border-radius:50%;background:#1f3a66;display:inline-block}
.arrow{position:absolute;top:171px;width:8px;height:8px;border-left:1px solid #ccc;border-bottom:1px solid #ccc}

/* services */
.services{position:absolute;left:0;top:1265px;width:100%;height:475px}
.service{position:absolute;width:270px;text-align:center}
.service.card{background:#fff;box-shadow:0 3px 16px rgba(0,0,0,.12)}
.service h3{font-size:19px;line-height:30px;color:var(--link);margin-top:10px}
.service p{font-size:12px;line-height:21px;color:var(--muted);margin:12px auto 0;width:240px}
.btn-line{display:inline-flex;align-items:center;justify-content:center;width:100px;height:33px;border:2px solid var(--blue);border-radius:17px;font-size:11.5px;color:var(--blue);margin-top:16px}

/* prospora band */
.band{position:absolute;left:0;top:1740px;width:100%;height:507px;background:radial-gradient(ellipse at 30% 80%,#3fb4f0 0%,#1670d2 35%,#0d3fa0 65%,#0a2a78 100%)}
.band-card{position:absolute;left:529px;top:71px;width:437px;height:365px;border-radius:14px;background:linear-gradient(135deg,#d8e1ec,#f1f6fa);text-align:center}
.band-card .mark{width:34px;height:34px;border-radius:50%;background:#e3a33a;margin:36px auto 0}
.band-card h3{font-size:23px;letter-spacing:4px;color:#333;margin-top:12px}
.band-card p{text-align:left;font-size:12px;line-height:21px;color:#444;margin:22px 31px 0}
.band-card .btn-red{position:relative;width:97px;height:29px;font-size:11.5px;margin:26px auto 0}

/* testimonials */
.voices{position:absolute;left:0;top:2247px;width:100%;height:440px;background:linear-gradient(180deg,#e5e5e5 0%,#eeeeee 60%,#f6f6f6 100%)}
.quote-box{position:absolute;left:135px;top:118px;width:785px;height:119px;background:#fff;border-radius:4px;text-align:center;font-style:italic;font-size:13px;line-height:21px;color:#333;padding:38px 40px 0}
.qmark{position:absolute;left:165px;top:85px;font-family:"Ubuntu",sans-serif;font-size:96px;line-height:96px;color:var(--red);font-weight:500}
.author{position:absolute;left:476px;top:263px;display:flex;align-items:center;gap:12px}
.author .avatar{width:42px;height:42px;border-radius:50%;background:#d4d4d4}
.author b{display:block;font-size:11.5px;color:#333;font-weight:600}
.author span{font-size:10.5px;color:var(--link)}
.dots{position:absolute;left:510px;top:342px;display:flex;gap:7px}
.dots i{width:4px;height:4px;border-radius:50%;background:#bbb}
.dots i.on{background:#333}

/* footer */
.footer{position:absolute;left:0;top:2645px;width:100%;height:370px;background:var(--navy);border-radius:50% 50% 0 0/40px 40px 0 0}
.fcol{position:absolute;top:102px}
.fcol h4{font-family:"Ubuntu",sans-serif;font-weight:400;font-size:15.5px;color:#fff}
.fcol h4::after{content:"";display:block;width:62px;height:1px;background:var(--red);margin-top:10px}
.fcol ul{list-style:none;margin-top:19px}
.fcol li{font-size:12.5px;color:#dfe6f3;height:25px;display:flex;align-items:center;gap:8px}
.fcol li::before{content:"";width:9px;height:9px;border-radius:50%;border:2px solid #3f7fd0;box-sizing:border-box}
.social{display:flex;gap:5px;margin-top:22px}
.social span{width:38px;height:38px;border-radius:50%;display:block}
.copy{position:absolute;left:89px;top:324px;font-size:12px;color:#fff}
.legal{position:absolute;right:89px;top:324px;font-size:12px;color:#9fb0d0;display:flex;gap:10px}
.legal em{font-style:normal;color:#4a5f8e}
</style>
</head>
<body>
<div class="site">

  <header class="masthead">
    <div class="brand"><span class="brand-dot"></span><span class="brand-name">Ledgerwise Reach</span></div>
    <nav class="nav"><span class="on">Home</span><span>About Us</span><span>Our Services</span><span>QA Technology</span><span>Intent Data</span><span>Contact Us</span></nav>
  </header>

  <section class="hero" role="img" aria-label="Softly moving dark blue abstract data wave background">
    <h1>The <span>Demand Generation</span> Company</h1>
    <p>Ledgerwise Reach offers multi-channel demand generation services to publishers and technology vendors through our network of lead generation websites and native speaking telemarketing agents. Whether looking for MQL, ABM or BANT campaigns, Ledgerwise Reach can assist you in delivering your demand generation strategy and generate pipeline for your sales teams and/or channel partners.</p>
    <a class="btn-red">Register Now</a>
  </section>
  <div class="hero-curve"></div>

  <section class="about">
    <h2>About Us</h2>
    <p style="top:595px">Ledgerwise Reach can deliver high quality sales leads from any country in the world. This can include leads via email or telemarketing, account-based targeting (ABM) or identifying need and pain points through BANT / SQL campaigns.</p>
    <p style="top:694px">Ledgerwise Reach offer expert demand generation support, from providing detailed leads of qualified decision-makers, to a comprehensive lead generation and SQL service.</p>
    <a class="btn-red">Read More</a>

    <div class="stat" style="left:742px;top:550px;height:152px">
      <svg width="30" height="28" viewBox="0 0 30 28" fill="none" stroke="#d1262c" stroke-width="1.6"><path d="M15 2v15M9 11l6 6 6-6M3 18v7h24v-7"/></svg>
      <div class="num">+70,000</div><div class="cap">Downloads Per Month</div>
    </div>
    <div class="stat" style="left:504px;top:726px;height:156px">
      <svg width="40" height="36" viewBox="0 0 40 36" fill="none" stroke="#d1262c" stroke-width="1.5"><circle cx="20" cy="8" r="5"/><circle cx="7" cy="26" r="5"/><circle cx="33" cy="26" r="5"/><path d="M16 12l-6 9M24 12l6 9M12 26h16"/></svg>
      <div class="num">+25,000</div><div class="cap">Leads Delivered Per Month</div>
    </div>
    <div class="stat" style="left:742px;top:726px;height:156px">
      <svg width="36" height="36" viewBox="0 0 36 36" fill="none" stroke="#d1262c" stroke-width="1.5"><circle cx="18" cy="18" r="15"/><path d="M3 18h30M18 3c-6 7-6 23 0 30M18 3c6 7 6 23 0 30"/></svg>
      <div class="num">+50</div><div class="cap">Countries We Can Reach</div>
    </div>
  </section>

  <section class="partners">
    <div class="section-title" style="top:47px">Who We Work With</div>
    <span class="arrow" style="left:104px;transform:rotate(45deg)"></span>
    <div class="partner-row">
      <span class="partner">Corvane</span>
      <span class="partner">QRT</span>
      <span class="partner">Tarvo</span>
      <span class="partner ring"><i></i>Dalvo</span>
      <span class="partner">Nimbrel</span>
      <span class="partner">Quellan</span>
      <span class="partner">Taskmere</span>
    </div>
    <span class="arrow" style="left:943px;transform:rotate(-135deg)"></span>
  </section>

  <section class="services">
    <div class="section-title" style="top:47px">Our Services</div>
    <div class="service" style="left:101px;top:120px">
      <svg width="66" height="66" viewBox="0 0 66 66" fill="none" stroke="#d1262c" stroke-width="1.6"><circle cx="33" cy="33" r="18" stroke-dasharray="4 4"/><path d="M33 21l3.5 7.5 8 1-6 5.5 1.6 8-7.1-4-7.1 4 1.6-8-6-5.5 8-1z"/></svg>
      <h3>Marketing Qualified Leads<br>(MQL)</h3>
      <p>A Marketing Qualified Lead (MQL) is a prospect that has expressed an interest in what your brand has to offer.</p>
      <a class="btn-line">Read More</a>
    </div>
    <div class="service" style="left:392px;top:120px">
      <svg width="66" height="66" viewBox="0 0 66 66" fill="none" stroke="#d1262c" stroke-width="1.6"><circle cx="33" cy="33" r="26"/><circle cx="33" cy="33" r="19"/><circle cx="33" cy="27" r="6"/><path d="M22 45c2-7 20-7 22 0"/></svg>
      <h3>Account Based Marketing<br>Leads (ABM)</h3>
      <p>ABM is a strategy that directs marketing resources to engaging a specific set of target accounts.</p>
      <a class="btn-line">Read More</a>
    </div>
    <div class="service card" style="left:685px;top:345px;height:0"></div>
    <div class="service card" style="left:685px;top:345px;top:345px;height:307px;margin-top:-200px">
      <svg width="60" height="66" viewBox="0 0 60 66" fill="none" stroke="#d1262c" stroke-width="1.6" style="margin-top:18px"><rect x="10" y="12" width="40" height="48" rx="3"/><path d="M22 12V6h16v6M18 38l14-8v22l-14-8zM36 38h6"/></svg>
      <h3>Sales Qualified Lead<br>BANT</h3>
      <p>An SQL lead or a BANT lead is a type of lead that expressed a specific interest in a product and service that you have to offer</p>
      <a class="btn-line">Read More</a>
    </div>
  </section>

  <section class="band" role="img" aria-label="Glowing blue digital particle landscape background">
    <div class="band-card">
      <div class="mark"></div>
      <h3>PROSPORA</h3>
      <p>Prospora is a proprietary lead verification platform from Ledgerwise Reach that aims to sift out invalid leads with questionable or erroneous data. The platform is designed to equip sales teams with accurate, high-quality records in order to improve lead generation, accelerate pipeline and increase revenue.</p>
      <a class="btn-red">Read More</a>
    </div>
  </section>

  <section class="voices" role="img" aria-label="Soft grey dotted background">
    <div class="section-title" style="top:50px">What Our Customers Say</div>
    <div class="quote-box">Lorem ipsum dolor sit amet, consectetur adipiscing elit. Ut elit tellus, luctus nec ullamcorper mattis, pulvinar dapibus leo.</div>
    <div class="qmark">&ldquo;</div>
    <div class="author"><span class="avatar"></span><div><b>Jon Maris</b><span>CEO</span></div></div>
    <div class="dots"><i></i><i class="on"></i><i></i></div>
  </section>

  <footer class="footer">
    <div class="fcol" style="left:89px"><h4>About Ledgerwise Reach</h4>
      <ul><li>About Us</li><li>QA Technology</li><li>Intent Data</li><li>Contact Us</li></ul></div>
    <div class="fcol" style="left:312px"><h4>SUPPORT</h4>
      <ul><li>Knowledge Base</li><li>Video Tutorials</li><li>Support Services</li><li>Contact Support</li></ul></div>
    <div class="fcol" style="left:535px"><h4>Services</h4>
      <ul><li>Marketing Qualified Leads</li><li>Account Based Marketing Leads</li><li>Sales Qualified Lead / BANT</li></ul></div>
    <div class="fcol" style="left:803px"><h4>Follow Us</h4>
      <div class="social"><span style="background:#3a62b0" aria-label="Social link one"></span><span style="background:#2f9be6" aria-label="Social link two"></span><span style="background:var(--red)" aria-label="Social link three"></span></div></div>
    <div class="copy">© Copyright 2020 Ledgerwise Reach co.</div>
    <div class="legal"><span>Privacy</span><em>|</em><span>Terms of Use</span><em>|</em><span>Sitemap</span></div>
  </footer>

</div>
</body>
</html>
```